Wood Bamboo Print Website

We like a brand new design for our wood bamboo print website. We print photo's and mount them on bamboo panels. trelvia dot com

We'd like a clean vintage/urban design

Design must at least contain:

Logo
Menu
Banner
The 2 options we have 2.5cm bamboo and 4cm bamboo hanging and standing
Upload photo button
Some text for UPS
LEt your imagination do the rest :)

Homepage
CMS page

Show responsive design

Design must be according bootstrap 3.0 rules

```html
<!DOCTYPE html>
<html lang="en">
<head>
<meta charset="utf-8">
<title>trelvia – real photos mounted on eco bamboo</title>
<link rel="stylesheet" href="https://fonts.googleapis.com/css2?family=Lato:wght@400;700;900&family=Niconne&display=swap">
<style>
:root{
  --wood-dark:#3a2a22;
  --wood-mid:#5b4338;
  --page:#ffffff;
  --panel:#e9e9e4;
  --panel-soft:#f1f1ee;
  --ribbon:#8d8d8d;
  --ribbon-dark:#6f6f6f;
  --green:#566530;
  --green-dark:#3f4b22;
  --text:#5b5b5b;
  --ink:#1d1d1d;
  --footer:#000000;
}
*{box-sizing:border-box;margin:0;padding:0}
html,body{width:1200px;height:2532px;overflow:hidden}
body{
  position:relative;
  background:linear-gradient(90deg,var(--wood-dark),var(--wood-mid) 30%,var(--wood-dark) 55%,var(--wood-mid) 80%,var(--wood-dark));
  font-family:"Lato",sans-serif;color:var(--text);
}
.abs{position:absolute}
.page{position:absolute;left:142px;top:48px;width:916px;height:2457px;background:var(--page);border-radius:26px}
/* header */
.brand{left:158px;top:74px}
.brand-name{font-family:"Lato",sans-serif;font-weight:400;font-size:78px;line-height:72px;color:var(--ink);letter-spacing:-2px}
.brand-tag{font-size:12px;font-weight:700;color:var(--ink);margin-top:4px;margin-left:2px}
.account{top:72px;right:158px;font-size:12px;color:#333;display:flex;gap:16px;align-items:center}
.account span{display:flex;align-items:center;gap:6px}
.account .sep{width:1px;height:14px;background:#bbb}
.cart{left:810px;top:106px;width:258px;height:46px;background:var(--green);color:#fff;font-size:12px;
  clip-path:polygon(0 0,100% 0,100% 100%,0 100%,16px 50%);display:flex;align-items:center;gap:10px;padding-left:36px;line-height:15px}
.nav{left:142px;top:190px;width:916px;height:36px;display:flex;border-bottom:1px solid #ddd}
.nav a{font-size:13.5px;color:#333;text-decoration:none;padding:6px 22px 0;position:relative}
.nav a+a{border-left:1px solid #ddd}
.nav a.active{border-bottom:3px solid var(--green);margin-left:18px;padding:6px 4px 0}
/* banner */
.banner{left:132px;top:241px;width:936px;height:471px;background:radial-gradient(circle at 55% 35%,#6f8f95 0,#8a8475 25%,#c9b48a 55%,#d9c296 75%,#8a7a5e 100%)}
.banner-caption{left:157px;top:600px;font-family:"Niconne",cursive;font-size:40px;line-height:42px;color:#2c2a20}
.arrow{top:456px}
/* ribbons */
.ribbon{height:46px;background:var(--ribbon);color:#fff;font-family:"Niconne",cursive;font-size:27px;line-height:46px;padding-left:22px;
  clip-path:polygon(0 0,100% 0,calc(100% - 18px) 50%,100% 100%,0 100%);
  background-image:repeating-linear-gradient(45deg,rgba(255,255,255,.06) 0 2px,transparent 2px 5px)}
.ribbon.right{clip-path:polygon(18px 0,100% 0,100% 100%,18px 100%,0 50%);padding-left:34px}
.panel{background:var(--panel)}
.card-text{font-size:13px;line-height:22px;color:var(--text)}
.btn{width:118px;height:36px;background:var(--green);color:#fff;font-size:13px;text-align:center;line-height:36px;
  border-radius:6px 6px 0 0;outline:1px dashed rgba(255,255,255,.55);outline-offset:-4px}
.photo{border:4px solid #d6d6d6;background:#fff}
.photo>div{width:100%;height:100%}
/* footer */
.footer{left:160px;top:2289px;width:880px;height:159px;background:var(--footer);color:#fff}
.fcol{top:20px;font-size:11.5px}
.fcol h4{font-family:"Niconne",cursive;font-weight:400;font-size:19px;margin-bottom:12px}
.fcol li{list-style:none;margin-bottom:9px;display:flex;align-items:center;gap:12px}
.fdiv{top:14px;width:1px;height:128px;background:#333}
.legal{left:160px;top:2448px;width:880px;height:37px;background:var(--green);color:#fff;font-size:11.5px;line-height:37px;padding:0 24px;display:flex;justify-content:space-between}
</style>
</head>
<body>
<div class="page"></div>

<header>
  <div class="abs brand"><div class="brand-name">trelvia</div><div class="brand-tag">real photos mounted on eco bamboo</div></div>
  <div class="abs account">
    <span><svg width="12" height="13"><rect x="1" y="6" width="10" height="7" fill="#333"/><path d="M3 6V4a3 3 0 0 1 6 0v2" stroke="#333" stroke-width="1.6" fill="none"/></svg>Login</span>
    <i class="sep"></i>
    <span><svg width="14" height="14"><rect x="1" y="3" width="10" height="10" fill="none" stroke="#333" stroke-width="1.5"/><path d="M5 9l8-8" stroke="#333" stroke-width="2"/></svg>Register</span>
  </div>
  <div class="abs cart">
    <svg width="26" height="22"><path d="M2 8h22l-3 12H5z" fill="none" stroke="#fff" stroke-width="2"/><path d="M8 8l5-6 5 6" fill="none" stroke="#fff" stroke-width="2"/></svg>
    <div>Shopping Cart:&nbsp; 0 Item(s)<br><b>(empty)</b></div>
  </div>
  <nav class="abs nav">
    <a class="active">Trelvia</a><a style="margin-left:18px">Trelvia Specs</a><a>Soorten Trelvia</a><a>Formaten &amp; Prijzen</a><a>Bestelinfo</a>
  </nav>
</header>

<section>
  <div class="abs banner" role="img" aria-label="Close-up of a printing press mounting a photo onto a bamboo panel"></div>
  <svg class="abs arrow" style="left:150px" width="24" height="40"><path d="M18 4L6 20l12 16" stroke="#fff" stroke-width="5" fill="none"/></svg>
  <svg class="abs arrow" style="left:1026px" width="24" height="40"><path d="M6 4l12 16L6 36" stroke="#fff" stroke-width="5" fill="none"/></svg>
  <div class="abs banner-caption">We print photo's and mount<br>them on bamboo panels.</div>
</section>

<!-- row 1 -->
<section>
  <div class="abs panel" style="left:160px;top:749px;width:281px;height:375px"></div>
  <div class="abs panel" style="left:460px;top:749px;width:280px;height:375px"></div>
  <div class="abs panel" style="left:760px;top:749px;width:280px;height:375px"></div>
  <div class="abs ribbon" style="left:150px;top:771px;width:262px">About Us</div>
  <div class="abs ribbon" style="left:450px;top:771px;width:262px">2,5 cm Bamboo</div>
  <div class="abs ribbon" style="left:750px;top:771px;width:262px">4 cm Bamboo</div>
  <p class="abs card-text" style="left:173px;top:838px;width:256px">Lorem ipsum dolor sit amet, consectetuer adipiscing elit, sed diam nonummy nibh euismod tincidunt ut laoreet dolore magna aliquam erat volutpat. Ut wisi enim ad minim veniam, quis nostrud exerci tation ullamcorper suscipit lobortis nisl ut aliquip ex ea commodo consequat. Duis autem vel eum iriure dolor in hendrerit in vulputate velit esse molestie consequat.</p>
  <div class="abs photo" style="left:470px;top:845px;width:260px;height:138px"><div role="img" aria-label="Two photos mounted on 2.5 cm bamboo blocks" style="background:linear-gradient(135deg,#6e7f86,#b88e6a,#d8c7a8)"></div></div>
  <div class="abs photo" style="left:770px;top:845px;width:260px;height:138px"><div role="img" aria-label="Photo mounted on a 4 cm bamboo block" style="background:linear-gradient(135deg,#d8c39a,#5f7d8c,#c59a72)"></div></div>
  <p class="abs card-text" style="left:473px;top:1000px;width:256px">Lorem ipsum dolor sit amet, consectetuer adipiscing elit, sed diam laoreet dolore magna aliquam erat volutpat.</p>
  <p class="abs card-text" style="left:773px;top:1000px;width:256px">Lorem ipsum dolor sit amet, consectetuer adipiscing elit, sed diam laoreet dolore magna aliquam erat volutpat.</p>
  <div class="abs btn" style="left:241px;top:1092px">Read More</div>
  <div class="abs btn" style="left:541px;top:1092px">Read More</div>
  <div class="abs btn" style="left:841px;top:1092px">Read More</div>
</section>

<!-- video / upload -->
<section>
  <div class="abs ribbon" style="left:132px;top:1168px;width:260px">Video</div>
  <div class="abs ribbon right" style="left:763px;top:1168px;width:305px">Upload your photo &amp; order</div>
  <div class="abs panel" style="left:160px;top:1246px;width:580px;height:324px;background:var(--panel-soft)"></div>
  <div class="abs" style="left:170px;top:1256px;width:562px;height:278px;background:linear-gradient(160deg,#7b6a7a,#cfc9b6 40%,#b48ab0 75%,#6a4c6c)" role="img" aria-label="Video still of photo blocks laid out on a table"></div>
  <svg class="abs" style="left:433px;top:1391px" width="36" height="36"><circle cx="18" cy="18" r="17" fill="#fff"/><path d="M14 10l11 8-11 8z" fill="#222"/></svg>
  <div class="abs" style="left:170px;top:1534px;width:562px;height:28px;background:#2a2a2a;color:#ddd;font-size:10px;display:flex;align-items:center;gap:8px;padding:0 8px">
    <svg width="10" height="10"><path d="M1 0l9 5-9 5z" fill="#ddd"/></svg>04:59
    <div style="flex:1;height:6px;border-radius:3px;background:#666;position:relative"><span style="position:absolute;left:20px;top:-3px;width:12px;height:12px;border-radius:50%;background:#c8d35a"></span></div>10:35
    <svg width="22" height="12"><path d="M1 4h4l4-3v10l-4-3H1z" fill="#ddd"/><path d="M14 2l7 8M14 10l7-8" stroke="#ddd" stroke-width="1.3"/></svg>
  </div>
  <div class="abs panel" style="left:760px;top:1246px;width:280px;height:324px;background:var(--panel-soft)"></div>
  <div class="abs" style="left:770px;top:1256px;width:260px;height:140px;border:5px solid var(--green);background:linear-gradient(135deg,#b7b3ad,#e4e1dc,#a9a4a0);display:flex;align-items:center;justify-content:center;text-align:center;font-weight:900;font-size:17px;color:#1c1c1c;line-height:24px">Drage image here<br>to upload photo</div>
  <p class="abs card-text" style="left:773px;top:1412px;width:256px">Upload hier je foto en bestel je Trelvia voor aan de muur of een block om neer te zetten! Bestellen gaat gemakkelijk in 3 stappen, uploaden, formaat selecteren en foto op maat maken.</p>
  <div class="abs btn" style="left:841px;top:1546px">Upload Photo</div>
</section>

<!-- gallery -->
<section>
  <div class="abs ribbon" style="left:132px;top:1614px;width:936px;clip-path:none">Gallery</div>
  <svg class="abs" style="left:990px;top:1620px" width="46" height="34"><path d="M20 2L6 17l14 15M26 2l14 15-14 15" stroke="#fff" stroke-width="1.5" fill="none"/></svg>
  <div class="abs panel" style="left:160px;top:1660px;width:880px;height:197px"></div>
  <div class="abs photo" style="left:188px;top:1688px;width:260px;height:140px"><div role="img" aria-label="Collection of bamboo photo blocks" style="background:linear-gradient(135deg,#8a9aa6,#e6dfd0,#7fb05a)"></div></div>
  <div class="abs photo" style="left:470px;top:1688px;width:260px;height:140px"><div role="img" aria-label="Portrait and close-up prints on bamboo" style="background:linear-gradient(135deg,#a38a70,#6d3a2a,#d1b58a)"></div></div>
  <div class="abs photo" style="left:752px;top:1688px;width:260px;height:140px"><div role="img" aria-label="Market photo mounted on bamboo block" style="background:linear-gradient(135deg,#d8c39a,#5f7d8c,#c59a72)"></div></div>
</section>

<!-- row 3 -->
<section>
  <div class="abs panel" style="left:160px;top:1884px;width:281px;height:378px;background:var(--panel-soft)"></div>
  <div class="abs panel" style="left:460px;top:1884px;width:280px;height:378px;background:var(--panel-soft)"></div>
  <div class="abs panel" style="left:760px;top:1884px;width:280px;height:378px;background:var(--panel-soft)"></div>
  <div class="abs ribbon" style="left:150px;top:1907px;width:262px">Quality</div>
  <div class="abs ribbon" style="left:450px;top:1907px;width:262px">Sizes and Prices</div>
  <div class="abs ribbon" style="left:750px;top:1907px;width:262px">Shipment</div>
  <div class="abs photo" style="left:168px;top:1979px;width:262px;height:140px"><div role="img" aria-label="Hands checking a bamboo panel" style="background:linear-gradient(135deg,#2a2620,#e8dcb8,#b8975e)"></div></div>
  <div class="abs photo" style="left:470px;top:1979px;width:260px;height:140px"><div role="img" aria-label="Bamboo blocks in various sizes" style="background:linear-gradient(135deg,#4a4038,#b89c74,#6b5a48)"></div></div>
  <div class="abs photo" style="left:770px;top:1979px;width:260px;height:140px"><div role="img" aria-label="Hands packing a bamboo panel for shipping" style="background:linear-gradient(135deg,#3c3228,#c89f62,#8a6a40)"></div></div>
  <p class="abs card-text" style="left:173px;top:2134px;width:256px">Lorem ipsum dolor sit amet, consectetuer adipiscing elit, sed diam laoreet dolore magna aliquam erat volutpat.</p>
  <p class="abs card-text" style="left:473px;top:2134px;width:256px">Lorem ipsum dolor sit amet, consectetuer adipiscing elit, sed diam laoreet dolore magna aliquam erat volutpat.</p>
  <p class="abs card-text" style="left:773px;top:2134px;width:256px">Lorem ipsum dolor sit amet, consectetuer adipiscing elit, sed diam laoreet dolore magna aliquam erat volutpat.</p>
  <div class="abs btn" style="left:241px;top:2227px">Read More</div>
  <div class="abs btn" style="left:541px;top:2227px">Read More</div>
  <div class="abs btn" style="left:841px;top:2227px">Read More</div>
</section>

<footer>
  <div class="abs footer">
    <div class="abs fcol" style="left:21px"><h4>Trelvia</h4><ul>
      <li><svg width="8" height="9"><path d="M0 0l8 4.5L0 9z" fill="#fff"/></svg>Environmentally Friendly</li>
      <li><svg width="8" height="9"><path d="M0 0l8 4.5L0 9z" fill="#fff"/></svg>Photos on Wood</li>
      <li><svg width="8" height="9"><path d="M0 0l8 4.5L0 9z" fill="#fff"/></svg>Trelvia Specs</li>
      <li><svg width="8" height="9"><path d="M0 0l8 4.5L0 9z" fill="#fff"/></svg>Types Trelvia</li></ul></div>
    <div class="abs fdiv" style="left:208px"></div>
    <div class="abs fcol" style="left:235px"><h4>Ordering Information</h4><ul>
      <li><svg width="8" height="9"><path d="M0 0l8 4.5L0 9z" fill="#fff"/></svg>Where to buy?</li>
      <li><svg width="8" height="9"><path d="M0 0l8 4.5L0 9z" fill="#fff"/></svg>Ordering info</li>
      <li><svg width="8" height="9"><path d="M0 0l8 4.5L0 9z" fill="#fff"/></svg>Sizes &amp; Prices</li></ul></div>
    <div class="abs fdiv" style="left:422px"></div>
    <div class="abs fcol" style="left:449px"><h4>Customer Service</h4><ul>
      <li><svg width="8" height="9"><path d="M0 0l8 4.5L0 9z" fill="#fff"/></svg>Shipping</li>
      <li><svg width="8" height="9"><path d="M0 0l8 4.5L0 9z" fill="#fff"/></svg>Makers Trelvia</li></ul></div>
    <div class="abs fdiv" style="left:610px"></div>
    <div class="abs fcol" style="left:638px;width:230px"><h4>Socialry</h4>
      <p style="line-height:16px">Like us on socialry and stay informed of our unique socialry actions!</p>
      <div style="margin-top:12px;width:152px;height:36px;background:#3b5998;display:flex;align-items:center;gap:10px;padding-left:8px;font-size:11.5px;font-weight:700">
        <span style="width:20px;height:20px;background:#fff;display:inline-block"></span>LIKE ON SOCIALRY</div>
    </div>
  </div>
  <div class="abs legal"><span>Contact &nbsp;|&nbsp; Privacy policy &nbsp;|&nbsp; General Conditions</span><span>Copyright 2014 trelvia. All Rights Reserved.</span></div>
</footer>
</body>
</html>
```